Tiltwave Drinks, Packaging Design Project

We need an awesome package design for Tiltwave Drinks' initial product launch.

Our company was founded with the idea of creating an innovative alcoholic beverage product that caters to a previously under-served market of millenials aged 21-30 who love to have a good time. The product will be served in a box with a plastic bladder and a spigot.

**Although our product will be served in a box similar to Cordelle or Hanna Strom, we are NOT in the wine category. TiltWave will focus on spirit based beverages.

We've chosen a great logo to use as the foundation for our package design. We will attach a jpeg version for your reference. You do NOT need to stick to the colors that we have used for the logo - but your colors should be bold, fun, and inviting.

We're looking forward to seeing your work!

-K7
Updates

Hey All!

Thanks so much for your contributions so far!! We want to clarify a couple things as we move forward.  Our product will be a spirit-based alcoholic beverage in a box.  We Tiltwave is more reminiscent of "portable jungle juice" rather than repackaged table wine.  We'll be looking at designs that aim younger and and are a little more daring.  We hope this helps to clarify our goals.

We're also looking at differentiating through alternative package dimensions.  Though we want to stay with a 5 liter size, we would be interested in looking at dimensions that look more like a boombox (longer and shorter than a Cordelle box).   

One possible combination would be 30 cm wide x 18 cm high x 11 cm deep.  Though you do not to adhere to these dimensions, we hope it will help by providing you with further direction.

Thanks SO much and we're looking forward to working with you!

 - K7

Industry/Entity Type

Plastic

```html
<!DOCTYPE html>
<html lang="en">
<head>
<meta charset="utf-8">
<title>Tiltwave Drinks – Box Panel</title>
<link rel="stylesheet" href="https://fonts.googleapis.com/css2?family=Jost:wght@500;800&display=swap">
<style>
  :root {
    --backdrop: #3a3a3b;
    --lime: #b4d334;
    --moss: #8ba63a;
    --deep-moss: #7c9a36;
    --magenta: #e0185c;
    --tangerine: #f05a28;
    --orange: #f7941d;
    --white: #ffffff;
  }
  * { margin: 0; padding: 0; box-sizing: border-box; }
  html, body {
    width: 1200px;
    height: 900px;
    overflow: hidden;
    background: var(--backdrop);
  }
  .box-panel {
    position: absolute;
    left: 76px;
    top: 144px;
    width: 1048px;
    height: 624px;
    overflow: hidden;
    background: var(--lime);
  }
  .panel-art {
    position: absolute;
    inset: 0;
    width: 100%;
    height: 100%;
  }
  .brand {
    position: absolute;
    left: 64px;
    top: 392px;
    width: 690px;
    font-family: "Jost", sans-serif;
    font-weight: 800;
    color: var(--magenta);
    text-align: right;
  }
  .brand-name {
    display: block;
    font-size: 150px;
    line-height: 1;
    letter-spacing: -2px;
    text-align: left;
  }
  .brand-line {
    display: block;
    font-size: 34px;
    line-height: 1;
    letter-spacing: 14px;
    margin-top: -4px;
    margin-right: -14px;
  }
</style>
</head>
<body>
  <main class="box-panel">
    <svg class="panel-art" viewBox="0 0 1048 624" xmlns="http://www.w3.org/2000/svg" aria-hidden="false">
      <!-- upper moss band -->
      <path class="band-moss-upper" fill="var(--moss)"
            d="M0 90 C200 70 420 110 620 120 C800 130 930 150 1048 170 L1048 260 C900 240 720 230 560 225 C380 220 200 200 0 190 Z"/>
      <!-- white stripes -->
      <path class="stripe-white-upper" fill="var(--white)"
            d="M0 92 C180 60 380 70 560 92 C760 118 920 140 1048 176 L1048 196 C900 168 740 140 560 116 C380 94 180 88 0 112 Z"/>
      <path class="stripe-white-lower" fill="var(--white)"
            d="M0 176 C200 182 400 200 600 210 C760 218 900 226 1048 222 L1048 240 C900 248 760 244 600 236 C400 226 200 210 0 200 Z"/>
      <!-- orange corner wedge -->
      <path class="wave-tangerine-left" fill="var(--tangerine)"
            d="M0 0 L260 0 C180 18 90 30 0 44 Z"/>
      <!-- magenta wave -->
      <path class="wave-magenta" fill="var(--magenta)"
            d="M100 0 L1048 0 L1048 186 C940 150 820 100 700 76 C560 50 380 40 150 54 C230 30 160 12 100 0 Z"/>
      <!-- orange sweep, right -->
      <path class="wave-tangerine-right" fill="var(--tangerine)"
            d="M780 96 C880 110 980 150 1048 190 L1048 310 C1000 250 940 200 860 160 C830 140 800 118 780 96 Z"/>
      <!-- lower moss ground -->
      <path class="ground-moss" fill="var(--deep-moss)"
            d="M0 382 C120 356 260 340 400 340 C560 340 720 350 860 330 C940 318 1000 300 1048 290 L1048 624 L0 624 Z"/>

      <!-- fruit illustration areas -->
      <ellipse class="fruit-strawberry" role="img" aria-label="Outline illustration of a strawberry"
               cx="110" cy="128" rx="68" ry="96" fill="var(--magenta)" fill-opacity="0.35"/>
      <ellipse class="fruit-leaf" role="img" aria-label="Outline illustration of a leaf"
               cx="310" cy="190" rx="82" ry="62" fill="var(--orange)" fill-opacity="0.35"/>
      <ellipse class="fruit-orange-slice-top" role="img" aria-label="Illustration of an orange slice"
               cx="410" cy="92" rx="82" ry="62" fill="var(--orange)" fill-opacity="0.55"/>
      <ellipse class="fruit-pear" role="img" aria-label="Outline illustration of a pear"
               cx="628" cy="146" rx="80" ry="112" fill="var(--tangerine)" fill-opacity="0.4"/>
      <ellipse class="fruit-orange-slice" role="img" aria-label="Illustration of an orange slice"
               cx="818" cy="250" rx="102" ry="82" fill="var(--tangerine)" fill-opacity="0.6"/>
      <ellipse class="fruit-apple" role="img" aria-label="Outline illustration of an apple"
               cx="1000" cy="356" rx="76" ry="122" fill="var(--tangerine)" fill-opacity="0.4"/>
    </svg>

    <h1 class="brand">
      <span class="brand-name">TILTWAVE</span>
      <span class="brand-line">DRINKS</span>
    </h1>
  </main>
</body>
</html>
```